Brindlemoor Copper Works

I created the attached in quill mark. I would like the background to look like black leather and the text to be gold. Any other suggestions would be appreciated. Thank you
Please note: all text now should be white .... sorry Partners changed their mind
Please remember when submitting designs, this design is for a folded business card with printing on all 4 sides ..... thank you
Also, the front of the card must have the wording above the logo. These will be placed in the wallet ID pockets and I would like to be able to read the wording.
Printing
I would like a folded business card. I created one in Quillmark but don't know how to send it to you to apply the final touches.

```html
<!DOCTYPE html>
<html lang="en">
<head>
<meta charset="utf-8">
<title>Brindlemoor Copper Works – Folded Business Card</title>
<link rel="stylesheet" href="https://fonts.googleapis.com/css2?family=Courgette&display=swap">
<style>
  :root {
    --leather-deep: #0a0b0c;
    --leather-mid: #131415;
    --leather-low: #18191a;
    --fold-line: #2e2e2f;
    --fold-shadow: #040404;
    --ink: #ffffff;
  }
  * { margin: 0; padding: 0; box-sizing: border-box; }
  html, body {
    width: 1200px;
    height: 693px;
    overflow: hidden;
    background: var(--leather-deep);
  }
  .card {
    position: relative;
    width: 1200px;
    height: 693px;
    font-family: "Courgette", cursive;
    color: var(--ink);
  }
  .panel-top {
    position: absolute;
    left: 0; top: 0;
    width: 1200px; height: 446px;
    background: radial-gradient(ellipse at 55% 45%, var(--leather-mid) 0%, var(--leather-deep) 80%);
  }
  .panel-bottom {
    position: absolute;
    left: 0; top: 446px;
    width: 1200px; height: 247px;
    background: linear-gradient(180deg, var(--leather-low) 0%, var(--leather-mid) 55%, #0e0f10 100%);
  }
  .leather-grain {
    position: absolute;
    left: 0; top: 0;
    width: 1200px; height: 693px;
    pointer-events: none;
  }
  .fold {
    position: absolute;
    left: 0; top: 444px;
    width: 1200px; height: 3px;
    background: linear-gradient(180deg, var(--fold-shadow), var(--fold-line));
  }
  .brand-mark {
    position: absolute;
    right: 54px;
    top: 262px;
    width: 200px;
    text-align: right;
  }
  .brand-dot {
    display: inline-block;
    width: 58px;
    height: 58px;
    border: 3px solid var(--ink);
    border-radius: 50%;
  }
  .brand-name {
    margin-top: 10px;
    font-size: 28px;
    line-height: 33px;
  }
  .contact {
    position: absolute;
    right: 54px;
    top: 481px;
    text-align: right;
    font-style: normal;
    font-size: 27px;
    line-height: 33px;
    letter-spacing: 0.5px;
  }
</style>
</head>
<body>
  <main class="card">
    <div class="panel-top"></div>
    <div class="panel-bottom"></div>

    <svg class="leather-grain" width="1200" height="693" viewBox="0 0 1200 693" aria-hidden="true">
      <defs>
        <filter id="grain-fine" x="0" y="0" width="100%" height="100%">
          <feTurbulence type="fractalNoise" baseFrequency="0.85" numOctaves="3" seed="4"/>
          <feColorMatrix type="matrix" values="0 0 0 0 1  0 0 0 0 1  0 0 0 0 1  0 0 0 0.09 0"/>
        </filter>
        <filter id="grain-crease" x="0" y="0" width="100%" height="100%">
          <feTurbulence type="turbulence" baseFrequency="0.035 0.06" numOctaves="2" seed="9"/>
          <feColorMatrix type="matrix" values="0 0 0 0 0  0 0 0 0 0  0 0 0 0 0  0 0 0 0.55 -0.1"/>
        </filter>
      </defs>
      <rect width="1200" height="693" filter="url(#grain-crease)" opacity="0.5"/>
      <rect width="1200" height="693" filter="url(#grain-fine)"/>
    </svg>

    <div class="fold"></div>

    <div class="brand-mark">
      <span class="brand-dot"></span>
      <div class="brand-name">Brindlemoor Copper Works</div>
    </div>

    <address class="contact">
      <div class="contact-name">Rowan &amp; Ada Lindqvist</div>
      <div class="contact-box">PO Box 412</div>
      <div class="contact-town">Marrowvale, Western Australia, 6399</div>
      <div class="contact-phone">Phone: 0400 555 218</div>
    </address>
  </main>
</body>
</html>
```